I am a company selling interior designing materials

HI, I am selling interior design materials and require a namecard which is more outstanding while following a certain details placement as attached.

My clients are mainly interior designers so it has to attract their attention rather than feeling that its "just another namecard". I am selling wallcoverings, fabrics, acoustics and carpets.

Target Market(s)

interior designers designing hotels, commerical offices.

Contact Information for Business Card

As per attached.
Please change address to 47 Jalan 16 Tampines #05-11 Vexor Tower Singapore 529341

Font styles to use
Other font styles liked:
• calibri

Requirements
Must have
• (1) company logo on top in the middle. Placement of contac details to be the same
• (2) company color is blue/green cymk 75/8/42/0
• (3) "KTV" logo to be prominent
• (4) You may change the logo but there should be a "swirl" surrounding the word KTV like current logo. The swirl pattern does not need to follow current logo and you may propose.
Should not have
• (1) there should not be any designs above "KTV" logo
• (2) no sharp triangles or angles

```html
<!DOCTYPE html>
<html lang="en">
<head>
<meta charset="utf-8">
<title>KTV Business Card</title>
<link href="https://fonts.googleapis.com/css2?family=Open+Sans:wght@400;600;700;800&display=swap" rel="stylesheet">
<style>
  :root {
    --teal: #2fb0a3;
    --red: #e3212b;
    --grey: #5b5b5b;
    --ink: #333333;
    --divider: #9a9a9a;
    --card: #ffffff;
    --stage: #3a3a3a;
  }
  * { margin: 0; padding: 0; box-sizing: border-box; }
  html, body { width: 1200px; height: 800px; overflow: hidden; }
  body {
    background: var(--stage);
    font-family: "Open Sans", sans-serif;
    display: flex;
    flex-direction: column;
    align-items: center;
    justify-content: center;
    gap: 30px;
  }
  .card {
    width: 620px;
    height: 354px;
    background: var(--card);
    position: relative;
  }
  /* Front */
  .card-front {
    display: flex;
    flex-direction: column;
    align-items: center;
  }
  .brand {
    display: flex;
    align-items: center;
    gap: 12px;
    margin-top: 70px;
  }
  .brand-dot {
    width: 18px; height: 18px;
    border-radius: 50%;
    background: var(--teal);
  }
  .brand-name {
    font-weight: 800;
    color: var(--grey);
    letter-spacing: 2px;
    line-height: 1;
  }
  .card-front .brand-name { font-size: 58px; }
  .company {
    margin-top: 16px;
    font-size: 17px;
    font-weight: 700;
    color: var(--grey);
  }
  .services {
    position: absolute;
    bottom: 56px;
    left: 0; right: 0;
    text-align: center;
    font-size: 16px;
    font-weight: 700;
    color: var(--red);
    word-spacing: 4px;
  }
  .services .sep { color: var(--ink); margin: 0 12px; font-weight: 400; }
  /* Back */
  .card-back { display: flex; align-items: center; }
  .card-back .brand {
    margin: 0;
    width: 350px;
    justify-content: center;
  }
  .card-back .brand-name { font-size: 84px; }
  .card-back .brand-dot { width: 24px; height: 24px; }
  .divider {
    width: 2px;
    height: 190px;
    background: var(--divider);
  }
  .contact { padding-left: 28px; color: var(--ink); }
  .person { font-size: 27px; font-weight: 700; color: var(--red); line-height: 1.1; }
  .role { font-size: 15px; font-weight: 600; color: var(--teal); margin-bottom: 12px; }
  .address { font-size: 12.5px; line-height: 1.45; margin-bottom: 8px; max-width: 220px; }
  .lines { list-style: none; font-size: 13px; line-height: 1.6; }
  .lines li { display: flex; align-items: center; gap: 8px; }
  .lines svg { width: 13px; height: 13px; fill: none; stroke: var(--teal); stroke-width: 2; stroke-linecap: round; stroke-linejoin: round; }
  .accent { color: var(--teal); }
</style>
</head>
<body>
  <section class="card card-front">
    <div class="brand">
      <span class="brand-name">KTV</span>
      <span class="brand-dot"></span>
    </div>
    <p class="company">Kavetra Interior Furnishings Pte Ltd</p>
    <p class="services">Wallcoverings<span class="sep">|</span>Acoustic<span class="sep">|</span>Fabrics<span class="sep">|</span>Carpet</p>
  </section>

  <section class="card card-back">
    <div class="brand">
      <span class="brand-name">KTV</span>
      <span class="brand-dot"></span>
    </div>
    <div class="divider"></div>
    <div class="contact">
      <p class="person">Daniel Reyes</p>
      <p class="role">Ceo &amp; Founder</p>
      <p class="address">47 Jalan 16 Tampines #05-11 Vexor Tower Singapore 529341</p>
      <ul class="lines">
        <li><svg viewBox="0 0 16 16"><path d="M4 2l2 3-1.5 1.5a8 8 0 0 0 5 5L11 10l3 2-1.5 2.5A11 11 0 0 1 1.5 3.5z"/></svg>(65) 9217 40563</li>
        <li><svg viewBox="0 0 16 16"><rect x="4" y="1.5" width="8" height="13" rx="1.5"/><path d="M7 12h2"/></svg>(65) 6382 7145</li>
        <li><svg viewBox="0 0 16 16"><rect x="1.5" y="3.5" width="13" height="9" rx="1"/><path d="M1.5 4l6.5 5 6.5-5"/></svg>hello@ktvfurnishings.com</li>
        <li><svg viewBox="0 0 16 16"><circle cx="7" cy="7" r="5"/><path d="M10.5 10.5L14.5 14.5"/></svg>www.<span class="accent">ktvfurnishings</span>.com</li>
      </ul>
    </div>
  </section>
</body>
</html>
```